2021 Personalized Vision Poster

A beautiful, pleasing design for my 2021 vision poster. Looking probably for an infographic. Open to shortening the wording used if able. As you will notice, each color represents a different category. Let me know if you need more details. The title of each section are mostly listed, but starting with the upper left with “my primary question” going counter-clockwise: my primary question, away values and rules, life purpose, power values (red), toward values and rules, top 4 goals for 2021 (middle), and relationship vision (middle). Basically, I’m just looking for a nice font and different formatting for my words.

Requirements
Must have
• All of the sections with a majority of the words used.
Nice to have
• Infographic would be nice, if possible. More concerned with a beautiful layout of words already expressed.
Should not have
• A complete reworking of the words used.

```html
<!DOCTYPE html>
<html lang="en">
<head>
<meta charset="utf-8">
<title>2021 – Live Courageously! Vision Poster</title>
<link rel="stylesheet" href="https://fonts.googleapis.com/css2?family=Graduate&family=Alfa+Slab+One&family=Montserrat:wght@800;900&family=Oswald:wght@500;600;700&family=Roboto:wght@400;500&family=Roboto+Slab:wght@700&family=Kalam:wght@400&display=swap">
<style>
  :root{
    --paper:#f1e4c4;
    --paper-light:#f8eed6;
    --navy:#245084;
    --teal:#0e7a6b;
    --teal-band:#17806f;
    --green:#4bb04f;
    --green-mid:#2a9a5e;
    --brown:#5a4530;
    --ribbon:#5b4128;
    --ink:#3a3a3a;
    --head:#5a4a2e;
    --red:#b3262a;
    --orange:#e58a2b;
    --note:#b5ef80;
  }
  *{margin:0;padding:0;box-sizing:border-box}
  html,body{width:1200px;height:848px;overflow:hidden}
  body{
    position:relative;
    background:radial-gradient(ellipse at 50% 45%,var(--paper-light) 0%,var(--paper) 70%,#e8d6ae 100%);
    font-family:"Roboto",sans-serif;color:var(--ink);
  }
  .abs{position:absolute}
  svg.layer{position:absolute;left:0;top:0;width:1200px;height:848px;overflow:visible}

  .title-text{font-family:"Graduate",serif;fill:var(--navy)}

  /* sticky note */
  .note{left:76px;top:156px;width:274px;height:192px;background:var(--note);
    transform:rotate(-2deg);box-shadow:4px 6px 10px rgba(0,0,0,.25);padding:22px 16px 0}
  .note p{font-family:"Kalam",cursive;font-size:19px;line-height:30px;text-align:center;color:#1d1d1d}
  .note .sig{font-family:"Roboto",sans-serif;font-weight:500;color:var(--navy);font-size:20px;
    margin-top:8px;text-align:right;padding-right:4px}
  .pin{left:200px;top:150px;width:16px;height:16px;border-radius:50%;background:var(--red);
    box-shadow:1px 2px 2px rgba(0,0,0,.3)}

  /* section headers */
  .bubble-head{font-family:"Oswald",sans-serif;font-weight:600;color:var(--head);letter-spacing:.5px;text-align:center}
  .bubble-sub{text-align:center}
  .away-head{left:77px;top:372px;width:237px;font-size:18px}
  .away-sub{left:77px;top:398px;width:237px;font-size:13px;color:#9e1a1a}
  .towards-head{left:831px;top:152px;width:290px;font-size:20px}
  .towards-sub{left:831px;top:183px;width:290px;font-size:14.5px;color:#222}

  /* tick lists */
  .list{list-style:none}
  .list li{position:relative;padding-left:22px}
  .list li svg{position:absolute;left:0;width:15px;height:15px}
  .away-list{left:76px;top:440px;width:270px;font-size:16px;line-height:19px}
  .away-list li{margin-bottom:8px}
  .away-list li svg{top:2px;color:var(--red)}
  .instead-head{left:74px;top:560px;font-family:"Roboto",sans-serif;font-weight:500;
    font-size:19px;color:var(--teal-band)}
  .instead-list{left:76px;top:592px;width:300px;font-size:15px;line-height:18px}
  .instead-list li{margin-bottom:4px}
  .instead-list li svg{top:2px;color:var(--orange)}
  .towards-list{left:838px;top:229px;width:300px;font-size:15.5px;line-height:19px}
  .towards-list li{padding-left:23px;margin-bottom:6.5px}
  .towards-list li svg{top:2px;color:var(--red)}
  .moving{left:831px;top:478px;width:310px;text-align:center;font-family:"Oswald",sans-serif;
    font-weight:600;font-size:20px;color:var(--navy)}

  /* relationship */
  .rel-fade{left:418px;top:540px;width:345px;height:180px;
    background:linear-gradient(180deg,rgba(255,255,255,.25),rgba(255,255,255,0))}
  .rel-list{font-size:24px;line-height:37px;color:#3d3d3d}
  .rel-list li{padding-left:32px}
  .rel-list li svg{top:8px;width:19px;height:19px;color:var(--red)}
  .rel-col1{left:439px;top:558px}
  .rel-col2{left:610px;top:558px}

  /* purpose band */
  .purpose{left:60px;top:750px;width:1080px;text-align:center;color:#fff;
    font-family:"Oswald",sans-serif;font-weight:700;font-size:23px;line-height:29px;
    letter-spacing:.4px;transform:rotate(-1.2deg)}

  .deco{position:absolute}
</style>
</head>
<body>

<svg width="0" height="0" style="position:absolute" aria-hidden="true">
  <symbol id="tick" viewBox="0 0 20 20">
    <path d="M16.5 6.5 A8 8 0 1 0 17.8 11" fill="none" stroke="currentColor" stroke-width="1.6"/>
    <path d="M5.5 9.5 L9 13 L18 3.5" fill="none" stroke="currentColor" stroke-width="2" stroke-linecap="round"/>
  </symbol>
</svg>

<!-- edge decorations -->
<div class="deco" role="img" aria-label="Kraft notebook with binder clip" style="left:0;top:266px;width:62px;height:140px;background:#c9a27a;transform:rotate(-12deg);transform-origin:left top;border-radius:3px"></div>
<div class="deco" role="img" aria-label="Black reading glasses" style="left:0;top:505px;width:50px;height:62px;border:5px solid #222;border-left:none;border-radius:0 40px 40px 0"></div>
<div class="deco" role="img" aria-label="Fountain pen" style="left:1168px;top:355px;width:12px;height:105px;background:linear-gradient(#222,#444);transform:rotate(25deg);border-radius:4px"></div>
<div class="deco" role="img" aria-label="Vintage typewriter with paper" style="left:1125px;top:500px;width:80px;height:172px;background:linear-gradient(170deg,#e9e9e9 0%,#dcdcdc 35%,#3c3c3c 36%,#1f1f1f 100%);border-radius:8px 0 0 16px"></div>

<svg class="layer" viewBox="0 0 1200 848" aria-hidden="false">
  <!-- title -->
  <text class="title-text" x="57" y="121" font-size="96" textLength="1088" lengthAdjust="spacingAndGlyphs">2021- LIVE COURAGEOUSLY!</text>

  <!-- away bubble -->
  <path d="M90 370 Q77 370 77 383 L77 404 Q77 414 95 416 L102 428 L104 418 Q200 424 300 414 Q314 410 314 398 L312 382 Q310 370 296 369 Z" fill="none" stroke="#555" stroke-width="1" stroke-dasharray="4 3"/>
  <!-- loop arrows -->
  <path d="M300 430 Q345 415 352 465 Q358 530 290 552 Q180 570 90 550 Q50 560 60 640 Q62 700 90 712 Q120 720 150 712" fill="none" stroke="#555" stroke-width="1" stroke-dasharray="4 3"/>
  <path d="M302 427 l6 -5 l-1 7 z" fill="var(--orange)"/>
  <path d="M150 712 l-6 -4 l0 7 z" fill="var(--orange)"/>

  <!-- towards bubble -->
  <path d="M845 148 Q831 150 832 165 L833 192 Q836 202 856 204 L861 218 L866 205 Q1000 214 1100 208 Q1122 204 1121 186 L1120 162 Q1118 146 1100 145 Q980 142 845 148 Z" fill="none" stroke="#555" stroke-width="1" stroke-dasharray="4 3"/>

  <!-- goals frame -->
  <path d="M497 177 L452 177 Q442 177 442 187 L442 483 M700 177 L739 177 Q749 177 749 187 L749 483" fill="none" stroke="#555" stroke-width="1" stroke-dasharray="2 2"/>
  <!-- TOP 4 banner -->
  <path d="M486 158 L711 158 L700 172 L711 201 Q598 189 486 201 L497 172 Z" fill="var(--teal-band)"/>
  <path d="M496 158 Q598 138 701 158 L701 172 Q598 156 496 172 Z" fill="var(--teal-band)"/>
  <text x="598" y="187" text-anchor="middle" font-family="'Alfa Slab One',serif" font-size="34" fill="#fff" stroke="#0b5e52" stroke-width="1">TOP 4</text>

  <text x="465" y="261" font-family="Montserrat,sans-serif" font-weight="900" font-size="60" fill="var(--green)" textLength="262" lengthAdjust="spacingAndGlyphs">RENTAL</text>
  <text x="465" y="316" font-family="Montserrat,sans-serif" font-weight="800" font-size="54" fill="var(--teal)" textLength="264" lengthAdjust="spacingAndGlyphs">175 LBS.</text>
  <text x="463" y="390" font-family="Montserrat,sans-serif" font-weight="900" font-size="76" fill="var(--green-mid)" textLength="260" lengthAdjust="spacingAndGlyphs">TEAM</text>
  <text x="466" y="446" font-family="Montserrat,sans-serif" font-weight="900" font-size="38" fill="var(--teal)">$</text>
  <text x="490" y="468" font-family="Montserrat,sans-serif" font-weight="900" font-size="80" fill="var(--teal)" textLength="234" lengthAdjust="spacingAndGlyphs">250K</text>

  <!-- relationship ribbon -->
  <path d="M414 492 Q450 480 505 490 L470 515 L505 540 Q460 528 420 540 L440 515 Z" fill="var(--ribbon)"/>
  <path d="M789 508 Q750 500 700 510 L732 535 L705 556 Q745 545 782 556 L760 530 Z" fill="var(--ribbon)"/>
  <path d="M470 498 Q600 470 740 480 L740 540 Q600 530 472 552 Z" fill="#6b4d30"/>
  <text x="488" y="534" font-family="'Roboto Slab',serif" font-weight="700" font-size="26" fill="#fff" transform="rotate(-4 600 520)" textLength="236" lengthAdjust="spacingAndGlyphs">Relationship Vision</text>

  <!-- power words -->
  <text x="847" y="565" font-family="Montserrat,sans-serif" font-weight="900" font-size="46" fill="var(--teal)" textLength="216" lengthAdjust="spacingAndGlyphs">POWER</text>
  <text x="847" y="604" font-family="Montserrat,sans-serif" font-weight="900" font-size="42" fill="var(--green-mid)" textLength="216" lengthAdjust="spacingAndGlyphs">COURAGE</text>
  <text x="884" y="687" font-family="Oswald,sans-serif" font-weight="700" font-size="44" fill="var(--navy)" transform="rotate(-90 884 687)" textLength="76" lengthAdjust="spacingAndGlyphs">JOY</text>
  <text x="886" y="687" font-family="Oswald,sans-serif" font-weight="700" font-size="104" fill="var(--brown)" textLength="177" lengthAdjust="spacingAndGlyphs">LOVE</text>
  <text x="1071" y="528" font-family="Montserrat,sans-serif" font-weight="800" font-size="31" fill="var(--green)" transform="rotate(90 1071 528)" textLength="159" lengthAdjust="spacingAndGlyphs">PRESENCE</text>

  <!-- purpose band -->
  <path d="M0 734 L40 728 L60 733 L120 725 L200 731 L300 722 L380 728 L500 720 L600 726 L700 718 L800 723 L900 716 L1000 721 L1100 713 L1200 718 L1200 848 L0 848 Z" fill="var(--navy)"/>
  <path d="M0 818 L100 814 L250 820 L400 812 L560 818 L700 811 L850 817 L1000 810 L1200 815 L1200 848 L0 848 Z" fill="var(--green)"/>
</svg>

<!-- primary question -->
<div class="abs pin"></div>
<div class="abs note">
  <p>How can I be even more grateful for the love in my heart for God, myself, and others?</p>
  <div class="sig">- My Primary Question</div>
</div>

<!-- away values -->
<div class="abs bubble-head away-head">AWAY VALUES AND RULES</div>
<div class="abs bubble-sub away-sub">Only if I were to avoid...</div>
<ul class="abs list away-list">
  <li><svg><use href="#tick"/></svg>Consistent, unrighteous anger</li>
  <li><svg><use href="#tick"/></svg>Consistent, debilitating, illusion of failure</li>
  <li><svg><use href="#tick"/></svg>Consistent, debilitating anxiety</li>
</ul>
<div class="abs instead-head">Instead of ...</div>
<ul class="abs list instead-list">
  <li><svg><use href="#tick"/></svg>Knowing that I alone have the power to choose to be angry</li>
  <li><svg><use href="#tick"/></svg>Realizing God has made me a conqueror I will not fail</li>
  <li><svg><use href="#tick"/></svg>Realizing God has given me all the inner peace I need</li>
</ul>

<!-- relationship vision -->
<div class="abs rel-fade"></div>
<ul class="abs list rel-list rel-col1">
  <li><svg><use href="#tick"/></svg>Love</li>
  <li><svg><use href="#tick"/></svg>Respect</li>
  <li><svg><use href="#tick"/></svg>Courage</li>
  <li><svg><use href="#tick"/></svg>Desire</li>
</ul>
<ul class="abs list rel-list rel-col2">
  <li><svg><use href="#tick"/></svg>Fun</li>
  <li><svg><use href="#tick"/></svg>Flirty</li>
  <li><svg><use href="#tick"/></svg>Romantic</li>
</ul>

<!-- towards values -->
<div class="abs bubble-head towards-head">TOWARDS VALUES &amp; RULES:</div>
<div class="abs bubble-sub towards-sub">Any time I am...</div>
<ul class="abs list towards-list">
  <li><svg><use href="#tick"/></svg>Giving of myself and serve others, OR</li>
  <li><svg><use href="#tick"/></svg>Accepting love from God or others, OR</li>
  <li><svg><use href="#tick"/></svg>Allowing myself to stay present, OR</li>
  <li><svg><use href="#tick"/></svg>Doing something even when scary, OR</li>
  <li><svg><use href="#tick"/></svg>Choosing to put myself first, OR</li>
  <li><svg><use href="#tick"/></svg>Protecting vulnerability, OR</li>
  <li><svg><use href="#tick"/></svg>Taking actions consistent with my identity, OR</li>
  <li><svg><use href="#tick"/></svg>Getting outdoors, OR</li>
  <li><svg><use href="#tick"/></svg>Going on a little or big adventure, OR</li>
</ul>
<div class="abs moving">MOVING MY BODY!</div>

<!-- life purpose -->
<div class="abs purpose">THE PURPOSE OF MY LIFE IS TO BE LOVING, COURAGEOUS, AND FUN! I SEEK ADVENTURE,<br>LAUGH AND PLAY, AND LIVE IN GOD'S IDENTITY FOR ME</div>

</body>
</html>
```